Custom Monogramming and Retail gifts

We need a Business Card for a monogramming business that offers many retail gift options. We are a home based business that uses social media (Chatterbook,clipboardly and our website) to sell our products. Our target market is college age, high school, baby gifts.
We want a preppy fun look. Monogramming is very popular in the South

Industry/Entity Type

College

Contact Information for Business Card

Threaded N' Charmed
Custom Monogramming and Gifts
5183 Larkmoor Lane
Fernhollow, ZZ 00512
Mona Prell, Owner
555-214-7390
threadedncharmed.example
threadedncharmed@mailbox.example

```html
<!DOCTYPE html>
<html lang="en">
<head>
<meta charset="utf-8">
<title>Threaded N' Charmed — Business Card</title>
<link rel="stylesheet" href="https://fonts.googleapis.com/css2?family=Arimo:wght@400;700&display=swap">
<style>
  :root {
    --backdrop: #e9e6e1;
    --card: #ffffff;
    --pink: #e6338a;
    --grey: #6f6f6f;
    --band-top: #3a3a3a;
    --band-dark: #151515;
  }
  * { margin: 0; padding: 0; box-sizing: border-box; }
  html, body {
    width: 1200px;
    height: 1000px;
    overflow: hidden;
    background: var(--backdrop);
    font-family: "Arimo", Arial, sans-serif;
  }
  .stage {
    width: 1200px;
    height: 1000px;
    display: flex;
    align-items: center;
    justify-content: center;
  }
  .business-card {
    position: relative;
    width: 980px;
    height: 560px;
    background: var(--card);
    box-shadow: 0 10px 30px rgba(0,0,0,0.15);
    overflow: hidden;
  }
  .brand {
    position: absolute;
    left: 56px;
    top: 190px;
    width: 330px;
    display: flex;
    align-items: center;
    gap: 14px;
  }
  .brand-dot {
    flex: none;
    width: 22px;
    height: 22px;
    border-radius: 50%;
    background: var(--pink);
  }
  .brand-name {
    font-size: 36px;
    line-height: 1.1;
    font-weight: 700;
    color: var(--pink);
  }
  .contact {
    position: absolute;
    left: 470px;
    top: 78px;
    color: var(--grey);
  }
  .contact-name {
    font-size: 30px;
    color: var(--pink);
    text-transform: uppercase;
    margin-bottom: 26px;
    letter-spacing: 0.5px;
  }
  .contact-name .role {
    color: var(--grey);
    text-transform: none;
    font-size: 26px;
  }
  .contact-list { list-style: none; }
  .contact-list li {
    display: flex;
    align-items: flex-start;
    gap: 14px;
    font-size: 24px;
    line-height: 34px;
  }
  .contact-list svg {
    flex: none;
    width: 20px;
    height: 20px;
    margin-top: 7px;
    fill: var(--pink);
  }
  .chevron-band {
    position: absolute;
    left: 0;
    right: 0;
    bottom: 0;
    height: 210px;
    background: linear-gradient(180deg, var(--band-top) 0%, var(--band-dark) 100%);
  }
</style>
</head>
<body>
<main class="stage">
  <article class="business-card">
    <div class="brand">
      <span class="brand-dot"></span>
      <span class="brand-name">Threaded N' Charmed</span>
    </div>

    <section class="contact">
      <p class="contact-name">Mona Prell <span class="role">Owner</span></p>
      <ul class="contact-list">
        <li>
          <svg viewBox="0 0 24 24" aria-hidden="true"><path d="M6.6 10.8a15.1 15.1 0 0 0 6.6 6.6l2.2-2.2c.3-.3.7-.4 1-.2 1.1.4 2.3.6 3.6.6.6 0 1 .4 1 1V20c0 .6-.4 1-1 1C10.6 21 3 13.4 3 4c0-.6.4-1 1-1h3.5c.6 0 1 .4 1 1 0 1.3.2 2.5.6 3.6.1.3 0 .7-.2 1z"/></svg>
          <span>555-214-7390</span>
        </li>
        <li>
          <svg viewBox="0 0 24 24" aria-hidden="true"><path d="M12 2a10 10 0 1 0 0 20 10 10 0 0 0 0-20zm6.9 6h-3a15.6 15.6 0 0 0-1.3-3.9A8 8 0 0 1 18.9 8zM12 4c.8 1.2 1.5 2.5 1.9 4h-3.8c.4-1.5 1.1-2.8 1.9-4zM4.3 14a8 8 0 0 1 0-4h3.4a16 16 0 0 0 0 4zm.8 2h3a15.6 15.6 0 0 0 1.3 3.9A8 8 0 0 1 5.1 16zm3-8h-3a8 8 0 0 1 4.3-3.9C8.8 5.3 8.4 6.6 8.1 8zM12 20c-.8-1.2-1.5-2.5-1.9-4h3.8c-.4 1.5-1.1 2.8-1.9 4zm2.3-6H9.7a14.7 14.7 0 0 1 0-4h4.6a14.7 14.7 0 0 1 0 4zm.3 5.9c.6-1.2 1-2.5 1.3-3.9h3a8 8 0 0 1-4.3 3.9zm1.7-5.9a16 16 0 0 0 0-4h3.4a8 8 0 0 1 0 4z"/></svg>
          <span>threadedncharmed.example</span>
        </li>
        <li>
          <svg viewBox="0 0 24 24" aria-hidden="true"><path d="M3 5h18c.6 0 1 .4 1 1v12c0 .6-.4 1-1 1H3c-.6 0-1-.4-1-1V6c0-.6.4-1 1-1zm1 2.3V17h16V7.3l-8 5.2z M5.2 7 12 11.4 18.8 7z"/></svg>
          <span>threadedncharmed@mailbox.example</span>
        </li>
        <li>
          <svg viewBox="0 0 24 24" aria-hidden="true"><path d="M12 3 2 12h3v8h5v-5h4v5h5v-8h3z"/></svg>
          <span>5183 Larkmoor Lane Fernhollow<br>ZZ 00512</span>
        </li>
      </ul>
    </section>

    <div class="chevron-band" role="img" aria-label="Black and white chevron stripe pattern band along the bottom of the card"></div>
  </article>
</main>
</body>
</html>
```